New manufacturing IT architecture concept powerpoint presentation

Create an appealing PowerPoint presentation, from handmade sketches, to illustrate a new approach to manufacturing IT architectures. We want to present the idea to augment the experience of people working in manufacturing plants using AI based on the data that our systems normally collect. We even want to present the power of having a tier 2 Manufacturing execution system that can coordinate and optimize production between multiple plants of the same corporate. The target audience is IT managers, Operations Managers, plant managers, engineering managers, and Continuous improvement managers.
Manufacturing companies mostly in Food & Bev and CPG. Mostly big multinational companies
Software manufacturing solutions (MES/MOM)
- Segoe

```html
<!DOCTYPE html>
<html lang="en">
<head>
<meta charset="utf-8">
<title>NEXA OPS – Manufacturing IT Architecture</title>
<link href="https://fonts.googleapis.com/css2?family=Roboto:wght@400;500;700;900&display=swap" rel="stylesheet">
<style>
:root{
  --page:#e9eaec;
  --white:#ffffff;
  --ink:#1d1f24;
  --muted:#5d6168;
  --teal:#33aeb0;
  --blue:#2270c0;
  --navy:#0c3a78;
  --red:#d3091f;
  --grid:#d9dbde;
  --photo-dark:#2b3d57;
  --photo-mid:#51657f;
}
*{box-sizing:border-box;margin:0;padding:0}
html,body{width:1200px;height:4051px;overflow:hidden}
body{background:var(--page);font-family:"Roboto",Arial,sans-serif;color:var(--ink);position:relative}
.slide{position:absolute;left:77px;width:1046px;height:588px;background:var(--white);overflow:hidden;box-shadow:0 6px 22px rgba(0,0,0,.14)}
.brand{position:absolute;right:58px;top:34px;font-weight:700;font-size:40px;letter-spacing:.5px;color:var(--blue);line-height:1}
.brand.light{color:var(--white)}
.slide-title{position:absolute;left:60px;top:33px;font-size:18px;font-weight:500;letter-spacing:.2px}
.title-rule{position:absolute;left:0;top:77px;width:708px;height:5px;background:var(--teal)}
.photo{position:absolute}
.cover .photo{inset:0;background:linear-gradient(120deg,#4a5d78 0%,#2d405c 55%,#1c2a40 100%)}
.cover-title{position:absolute;left:60px;top:232px;color:var(--white);font-size:28px;font-weight:700;line-height:45px;letter-spacing:.2px}
.tech-head{position:absolute;left:623px;top:238px;font-size:25px;font-weight:500}
.tech-text{position:absolute;left:623px;top:285px;width:372px;font-size:16.5px;line-height:29px;color:var(--muted)}
.lead{position:absolute;left:58px;top:122px;font-size:19px;font-weight:500}
.challenge{position:absolute;left:57px;display:flex;align-items:center;gap:24px;font-size:16px;line-height:26px;color:var(--muted)}
.icon-dot{width:68px;height:68px;border-radius:50%;background:var(--white);box-shadow:0 2px 10px rgba(0,0,0,.16);display:flex;align-items:center;justify-content:center;flex:none}
.challenge p{width:372px}
.expert-photo{left:576px;top:135px;width:411px;height:382px;background:radial-gradient(circle at 60% 35%,#3b7aa6 0%,#1e3550 45%,#0f1a2a 100%)}
.node-label{position:absolute;font-size:14px;font-weight:700;letter-spacing:.3px}
.node-label.left{text-align:right;width:120px}
.legend{position:absolute;top:544px;display:flex;align-items:center;gap:16px;font-size:17px}
.swatch{width:62px;height:22px}
.closing .photo{inset:0;background:linear-gradient(135deg,#3b4c63 0%,#243347 60%,#1b2535 100%)}
.thanks{position:absolute;left:0;right:0;top:232px;text-align:center;color:var(--white);font-size:78px;font-weight:900;letter-spacing:-1px;text-shadow:0 3px 10px rgba(0,0,0,.3)}
.contact{position:absolute;top:488px;display:flex;align-items:center;gap:20px;color:var(--white);font-size:16px;line-height:22px;font-weight:500}
.contact-dot{width:66px;height:66px;border-radius:50%;background:var(--white);border:6px solid rgba(255,255,255,.45);background-clip:padding-box;display:flex;align-items:center;justify-content:center;flex:none}
</style>
</head>
<body>

<section class="slide cover" style="top:88px">
  <div class="photo" role="img" aria-label="Engineer working at computer monitors in a factory control room"></div>
  <svg width="1046" height="588" style="position:absolute;inset:0">
    <polygon points="0,0 85,0 0,85" fill="#ffffff"/>
    <polygon points="85,0 130,0 20,110 20,588 0,588 0,85" fill="var(--teal)"/>
  </svg>
  <div class="brand light">NEXA OPS</div>
  <h1 class="cover-title">UNIFIED OPERATION CENTER &amp;<br>AUGMENTED OPERATION<br>MANAGEMENT</h1>
</section>

<section class="slide" style="top:738px">
  <svg width="1046" height="588" style="position:absolute;inset:0">
    <polygon points="0,0 673,0 371,588 0,588" fill="var(--photo-mid)" role="img" aria-label="Hand operating a tablet dashboard beside a robotic arm"/>
    <polygon points="582,130 642,0 673,0 411,510 385,560" fill="var(--blue)"/>
    <polygon points="641,115 660,115 405,588 386,588" fill="var(--teal)"/>
  </svg>
  <div class="brand">NEXA OPS</div>
  <h2 class="tech-head">OUR TECHNOLOGY</h2>
  <p class="tech-text">How digitalization evolved in last years from<br>being technology focused to user and value<br>focused</p>
</section>

<section class="slide" style="top:1397px">
  <h2 class="slide-title">SUBJECT MATTTER EXPERT</h2>
  <div class="title-rule"></div>
  <div class="brand">NEXA OPS</div>
  <p class="lead">Main challenged companies face today:</p>
  <div class="challenge" style="top:170px"><span class="icon-dot"><svg width="30" height="30" viewBox="0 0 30 30" fill="none" stroke="var(--blue)" stroke-width="1.8"><circle cx="15" cy="15" r="11"/><path d="M15 22v-8M15 16c-4 0-6-3-6-6 4 0 6 2 6 6zM15 14c0-3 2-5 5-5 0 3-2 5-5 5z"/></svg></span><p>Sustainability</p></div>
  <div class="challenge" style="top:249px"><span class="icon-dot"><svg width="30" height="30" viewBox="0 0 30 30" fill="none" stroke="var(--blue)" stroke-width="1.8"><path d="M15 4l10 6v10l-10 6-10-6V10z"/><path d="M5 10l10 6 10-6M15 16v10"/></svg></span><p>Flexibility ⟶ availability of assets, experience<br>(SMEs), decisions</p></div>
  <div class="challenge" style="top:331px"><span class="icon-dot"><svg width="30" height="30" viewBox="0 0 30 30" fill="none" stroke="var(--blue)" stroke-width="1.8"><circle cx="15" cy="15" r="10"/><circle cx="15" cy="15" r="4"/><path d="M15 2v5M15 23v5M2 15h5M23 15h5"/></svg></span><p>Workforce demographic ⟶ experience, decisions</p></div>
  <div class="challenge" style="top:413px"><span class="icon-dot"><svg width="30" height="30" viewBox="0 0 30 30" fill="none" stroke="var(--blue)" stroke-width="1.8"><rect x="4" y="6" width="22" height="18"/><circle cx="15" cy="15" r="2.5"/><path d="M9 10l4 3M21 10l-4 3M9 20l4-3M21 20l-4-3"/></svg></span><p>Corporate wide visibility and coordination</p></div>
  <div class="challenge" style="top:495px"><span class="icon-dot"><svg width="30" height="30" viewBox="0 0 30 30" fill="none" stroke="var(--blue)" stroke-width="1.8"><circle cx="15" cy="15" r="11"/><rect x="10" y="10" width="10" height="10"/><path d="M26 15l-3-3M4 15l3 3"/></svg></span><p>Supply Chain visibility and coordination</p></div>
  <div class="photo expert-photo" role="img" aria-label="Hands typing on a laptop with glowing cloud and data icons overlaid"></div>
</section>

<section class="slide" style="top:2056px">
  <h2 class="slide-title">OUR ACTIVITY</h2>
  <div class="title-rule"></div>
  <div class="brand">NEXA OPS</div>
  <svg width="1046" height="588" style="position:absolute;inset:0" fill="none">
    <g stroke="var(--teal)" stroke-width="1.5">
      <circle cx="522" cy="291" r="132"/>
      <path d="M321 138H380L429 198M723 138H664L615 198M321 291H390M654 291H723M321 444H380L429 384M723 444H664L615 384M522 423V459"/>
    </g>
    <g fill="#fff" stroke="var(--teal)" stroke-width="1.5">
      <circle cx="429" cy="198" r="4"/><circle cx="615" cy="198" r="4"/><circle cx="390" cy="291" r="4"/><circle cx="654" cy="291" r="4"/><circle cx="429" cy="384" r="4"/><circle cx="615" cy="384" r="4"/><circle cx="522" cy="423" r="4"/>
    </g>
    <circle cx="522" cy="291" r="110" fill="#5a4b3e" role="img" aria-label="Two engineers reviewing production data on a screen"/>
    <g filter="drop-shadow(0 2px 5px rgba(0,0,0,.18))" fill="#fff">
      <circle cx="286" cy="138" r="35"/><circle cx="758" cy="138" r="35"/><circle cx="286" cy="291" r="35"/><circle cx="758" cy="291" r="35"/><circle cx="286" cy="444" r="35"/><circle cx="758" cy="444" r="35"/><circle cx="522" cy="494" r="35"/>
    </g>
    <g stroke="var(--blue)" stroke-width="2.2">
      <circle cx="286" cy="138" r="11"/><circle cx="286" cy="138" r="4"/>
      <rect x="749" y="126" width="18" height="20" rx="4"/><path d="M749 138h18M752 150l-3 4M764 150l3 4"/>
      <circle cx="286" cy="291" r="3"/><path d="M286 291l-9-9M286 291l9-9M286 291l-9 9M286 291l9 9"/><circle cx="276" cy="281" r="2.5"/><circle cx="296" cy="281" r="2.5"/><circle cx="276" cy="301" r="2.5"/><circle cx="296" cy="301" r="2.5"/>
      <circle cx="758" cy="291" r="13"/><path d="M758 287v11M758 283v1"/>
      <path d="M275 440a12 12 0 0 1 22 0M275 450a12 12 0 0 0 22 0"/><circle cx="286" cy="445" r="3"/>
      <rect x="750" y="434" width="16" height="20" rx="2"/><path d="M758 440l4 3-4 3-4-3z"/>
      <rect x="511" y="487" width="14" height="14"/><rect x="518" y="480" width="14" height="14"/>
    </g>
  </svg>
  <div class="node-label left" style="left:110px;top:129px">SKILL</div>
  <div class="node-label" style="left:818px;top:129px">TRAIN</div>
  <div class="node-label left" style="left:110px;top:282px">CONNECT</div>
  <div class="node-label" style="left:818px;top:282px">INFORM</div>
  <div class="node-label left" style="left:110px;top:435px">COORDINATE</div>
  <div class="node-label" style="left:818px;top:435px">AUGMENT</div>
  <div class="node-label" style="left:492px;top:546px;width:60px;text-align:center">UNIFY</div>
</section>

<section class="slide" style="top:2715px">
  <h2 class="slide-title">WORKFORCE TURNOVER ⟶ MISSING EXPERIENCE</h2>
  <div class="title-rule"></div>
  <div class="brand">NEXA OPS</div>
  <svg width="1046" height="588" style="position:absolute;inset:0" font-family="Roboto, Arial, sans-serif" font-size="10" fill="#555">
    <g stroke="var(--grid)" stroke-width="1">
      <path d="M104 176H953M104 223H953M104 270H953M104 317H953M104 365H953M104 412H953"/>
      <path d="M104 459H953" stroke="#bbb"/>
    </g>
    <g text-anchor="end">
      <text x="96" y="180">6</text><text x="96" y="227">5</text><text x="96" y="274">4</text><text x="96" y="321">3</text><text x="96" y="369">2</text><text x="96" y="416">1</text><text x="96" y="463">0</text>
    </g>
    <g text-anchor="middle">
      <text x="173" y="479">t1</text><text x="255" y="479">t2</text><text x="337" y="479">t3</text><text x="418" y="479">t4</text><text x="500" y="479">t5</text><text x="582" y="479">t6</text><text x="664" y="479">t7</text><text x="746" y="479">t8</text><text x="828" y="479">t9</text><text x="909" y="479">t10</text>
    </g>
    <polyline fill="none" stroke="var(--red)" stroke-width="1.6" points="104,339 188,339 272,325 356,313 440,315 524,325 608,306 692,273 776,239 860,223 944,195"/>
    <polyline fill="none" stroke="var(--navy)" stroke-width="1.6" points="104,353 188,353 272,339 356,317 440,280 524,261 608,254 692,230 776,216 860,190 944,180"/>
  </svg>
  <div class="legend" style="left:331px"><span class="swatch" style="background:var(--red)"></span>Knowledge</div>
  <div class="legend" style="left:545px"><span class="swatch" style="background:var(--navy)"></span>Experience</div>
</section>

<section class="slide closing" style="top:3374px">
  <div class="photo" role="img" aria-label="Industrial machinery with sparks and a hand using a tablet"></div>
  <svg width="1046" height="588" style="position:absolute;inset:0">
    <polygon points="458,0 1046,0 1046,588 741,588" fill="var(--teal)" opacity=".82"/>
  </svg>
  <div class="brand light">NEXA OPS</div>
  <div class="thanks">THANK YOU</div>
  <div class="contact" style="left:88px">
    <span class="contact-dot"><svg width="22" height="26" viewBox="0 0 22 26"><path d="M11 1a9 9 0 0 0-9 9c0 7 9 15 9 15s9-8 9-15a9 9 0 0 0-9-9z" fill="var(--teal)"/><circle cx="11" cy="10" r="3.5" fill="#fff"/></svg></span>
    <span>27 Harbor Lane,<br>Springfield</span>
  </div>
  <div class="contact" style="left:429px">
    <span class="contact-dot"><svg width="24" height="24" viewBox="0 0 24 24"><path d="M6 2l4 5-2 3c1 3 3 5 6 6l3-2 5 4-2 4C10 22 2 14 2 4z" fill="var(--teal)"/></svg></span>
    <span>+1 (555) 014 2290</span>
  </div>
  <div class="contact" style="left:725px">
    <span class="contact-dot"><svg width="26" height="20" viewBox="0 0 26 20"><rect x="1" y="1" width="24" height="18" rx="2" fill="var(--teal)"/><path d="M2 3l11 8 11-8" fill="none" stroke="#fff" stroke-width="2"/></svg></span>
    <span>info@nexaops.com</span>
  </div>
</section>

</body>
</html>
```